Letterhead Design Project

I need a letterhead design that uses the same design ideas as my business card, which I have attached. I need it to look professional but also fresh and clean. If possible I would also like a with compliments slip and envelope designed as well.

I have attached a copy of a sample word doc for the letterhead that shows everything that must be on it. I would also like an alternative with all of the information in the header. The with compliments slip must also have the same information on it.
With regards to the envelope I only really need the logo and my po box address.

Target Market(s)

30+ Professionals

Industry/Entity Type

Business

Requirements
Must have
• I have attached a copy of a sample word doc for the letterhead that shows everything that must be on it. I would also like an alternative with all of the information in the header. The with compliments slip must also have the same information on it.
Should not have
• I am not looking for anything with traditional text as I can do that myself. I am looking for something that will stand out from the crowd.

```html
<!DOCTYPE html>
<html lang="en">
<head>
<meta charset="utf-8">
<title>Halden Insurance Letterhead</title>
<link rel="stylesheet" href="https://fonts.googleapis.com/css2?family=Source+Sans+3:wght@400&display=swap">
<style>
  :root {
    --backdrop: #d8d5d1;
    --paper: #ffffff;
    --ink: #2f2f31;
    --accent: #e8383d;
    --band-dark: #333335;
  }
  * { margin: 0; padding: 0; box-sizing: border-box; }
  html, body {
    width: 1200px; height: 900px; overflow: hidden;
    background: var(--backdrop);
    font-family: "Source Sans 3", "Helvetica Neue", Arial, sans-serif;
  }
  .letterhead {
    position: absolute; left: 264px; top: 15px;
    width: 672px; height: 870px;
    background: var(--paper);
    box-shadow: 0 4px 18px rgba(0,0,0,0.18);
  }
  .brand-name {
    position: absolute; left: 40px; top: 62px;
    font-size: 30px; font-weight: 400; color: var(--ink);
    line-height: 1;
  }
  .contact {
    position: absolute; left: 466px; top: 34px;
    font-size: 11.5px; line-height: 14px; color: var(--ink);
    list-style: none;
  }
  .contact .gap { margin-top: 14px; }
  .contact li { display: flex; align-items: center; gap: 5px; white-space: nowrap; }
  .contact svg { width: 10px; height: 10px; flex: none; }
  .legal {
    position: absolute; left: 0; right: 0; top: 802px;
    text-align: center; font-size: 8.4px; line-height: 11px; color: var(--ink);
  }
  .band-accent {
    position: absolute; left: 0; right: 0; top: 834px; height: 12px;
    background: var(--accent);
  }
  .band-dark {
    position: absolute; left: 0; right: 0; top: 846px; height: 24px;
    background: var(--band-dark);
  }
</style>
</head>
<body>
  <main class="letterhead">
    <header>
      <p class="brand-name">Halden Insurance</p>
    </header>

    <ul class="contact">
      <li>Level 2, 48 Ridgeway Road</li>
      <li>Norwood&nbsp; SA&nbsp; 5067</li>
      <li class="gap">PO Box 712, Kensington&nbsp; SA&nbsp; 5068</li>
      <li>
        <svg viewBox="0 0 10 10" aria-hidden="true"><rect x="2.5" y="0.5" width="5" height="9" rx="1" fill="var(--accent)"/><rect x="3.5" y="1.8" width="3" height="5.5" fill="#fff"/></svg>
        0400 123 456
      </li>
      <li>
        <svg viewBox="0 0 10 10" aria-hidden="true"><path d="M1 3.5 Q5 0.5 9 3.5 L8 5 L6.5 4.2 L6.5 3.3 Q5 2.8 3.5 3.3 L3.5 4.2 L2 5 Z" fill="var(--accent)"/><rect x="2" y="5.5" width="6" height="3.5" rx="0.6" fill="var(--accent)"/></svg>
        08 8000 4321
      </li>
      <li>
        <svg viewBox="0 0 10 10" aria-hidden="true"><rect x="0.8" y="2" width="8.4" height="6" fill="none" stroke="var(--accent)" stroke-width="1.1"/><path d="M0.8 2 L5 5.5 L9.2 2" fill="none" stroke="var(--accent)" stroke-width="1.1"/></svg>
        info@haldeninsurance.com.au
      </li>
      <li>www.haldeninsurance.com.au</li>
    </ul>

    <footer class="legal">
      <p>Halden Insurance Services Pty Ltd&nbsp;&nbsp; ABN 00 000 000 000 AR No 000000 as Authorised Representative of</p>
      <p>Marlow Insurance Group Pty Ltd ACN 000 000 000 ABN 11 111 111 111 AFS Licence No 111111</p>
    </footer>
    <div class="band-accent"></div>
    <div class="band-dark"></div>
  </main>
</body>
</html>
```